Curtain Cleaning Flyer to be designed for Singapore market

We are a laundry company providing curtain cleaning services to Singapore market. We have a company vehicle pickup and provide dismantling of curtain at customer house. The dismantled curtain will be weighed and quote will be given to customer immediately. If they accept the price, we will delivered and installed the clean curtain to them.
Refer to our website for more information https://www.glintora.com.sg/curtain-cleaning
The flyer will be distributed to higher income level people in Singapore staying in condominium/semi detached or bungalow.
I need a well designed flyers to engage people to use my service. So please help.

Target Market(s)

Singapore market

Industry/Entity Type

It Company

Requirements
Must have
• MUST INCLUDE CURTAINS pictures in design to let people know it is for curtain laundry
• 1) Flyer has to be eye catching and engage people to call and use our curtain cleaning services.
• 2) It has to professional.
• 3) It has to provide clear information of the following (see curtain cleaning picture I have provided)
• Curtain Laundry at $10/kg
• Call 8362 4915
• No Hidden Cost
• Include Pickup, Dismantle, Installation and Delivery
• 4) Provide company information:
• KORU FLINT, Reg No.71846302K
• 47 Merrowby Lane
• Singapore 071934
• https://www.glintora.com.sg/curtain-cleaning
• Email: enquiries@glintora.com.sg
• Tel: +65 8362 4915
• 5) Include our company logo but do not use it extensively.
Nice to have
• Nice to have a compelling action design for people to call and use my service.
• Nice to highlight on the good laundry price $10 per kg for curtain laundry
• Nice to be professional and cute
Should not have
• Complicated
• No design on woman wearing low cut dresses for promotion

```html
<!DOCTYPE html>
<html lang="en">
<head>
<meta charset="utf-8">
<title>Koru Flint – Curtain Laundry Flyer</title>
<link href="https://fonts.googleapis.com/css2?family=Oswald:wght@500;700&family=Open+Sans:wght@400;600&family=Montserrat:wght@800&display=swap" rel="stylesheet">
<style>
  :root {
    --sky: #2cb3e6;
    --sky-light: #5cc6ee;
    --ink: #111111;
    --paper: #ffffff;
    --backdrop: #eeeeee;
    --text: #222222;
  }
  * { margin: 0; padding: 0; box-sizing: border-box; }
  html, body { width: 1200px; height: 1200px; overflow: hidden; background: var(--backdrop); }
  .flyer {
    position: absolute; left: 194px; top: 31px;
    width: 738px; height: 1035px;
    background: var(--paper);
    transform: scale(1.1); transform-origin: 0 0;
    overflow: hidden;
    box-shadow: 0 4px 18px rgba(0,0,0,.15);
    font-family: "Open Sans", sans-serif; color: var(--text);
  }
  .brand {
    position: absolute; top: 48px; left: 0; width: 100%;
    display: flex; justify-content: center; align-items: center; gap: 14px;
  }
  .brand-dot { width: 38px; height: 38px; border-radius: 50%; background: var(--sky); }
  .brand-name {
    font-family: "Oswald", sans-serif; font-weight: 700; font-size: 46px;
    color: var(--sky); letter-spacing: 2px;
  }
  .hero-photo {
    position: absolute; left: 0; top: 208px; width: 460px; height: 340px;
    background: linear-gradient(135deg, #c9c4b6 0%, #8d8a80 45%, #5f5d57 70%, #b8b3a6 100%);
  }
  .offer-panel { position: absolute; left: 0; top: 190px; width: 738px; height: 378px; }
  .offer-text { position: absolute; left: 436px; top: 255px; font-family: "Oswald", sans-serif; font-weight: 700; }
  .offer-text .headline { font-size: 78px; line-height: 82px; color: var(--paper); letter-spacing: 1px; }
  .offer-text .sub { font-size: 50px; line-height: 52px; color: rgba(255,255,255,.7); font-weight: 500; letter-spacing: 1px; }
  .offer-text .price { font-size: 92px; line-height: 100px; color: var(--ink); margin-top: 2px; }
  .services { position: absolute; left: 24px; top: 600px; display: grid; grid-template-columns: 187px 180px; row-gap: 8px; }
  .service { display: flex; align-items: center; gap: 8px; font-weight: 600; font-size: 15px; }
  .service svg { width: 30px; height: 30px; flex: none; }
  .guarantee { position: absolute; right: 24px; top: 596px; text-align: right; }
  .guarantee .line1 { font-family: "Oswald", sans-serif; font-weight: 500; font-size: 54px; line-height: 58px; color: var(--ink); letter-spacing: 1px; }
  .guarantee .line2 { font-family: "Montserrat", sans-serif; font-weight: 800; font-size: 66px; line-height: 66px; color: var(--sky); letter-spacing: 4px; }
  .call-band { position: absolute; left: 0; top: 730px; width: 100%; height: 75px; background: var(--ink); }
  .call-band .cta { position: absolute; left: 436px; top: 8px; font-family: "Oswald", sans-serif; font-weight: 700; font-size: 42px; color: var(--paper); letter-spacing: 1px; }
  .call-band .cta span { color: var(--sky); }
  .shop-photo {
    position: absolute; top: 685px; width: 166px; height: 166px; border-radius: 50%;
    border: 5px solid var(--paper); box-shadow: 0 0 0 4px var(--sky);
  }
  .shop-photo.interior { left: 15px; background: linear-gradient(180deg, #f4f4f4 0%, #dde3e8 45%, #6d7378 75%, #9aa0a4 100%); }
  .shop-photo.storefront { left: 210px; background: linear-gradient(180deg, #1f4fa8 0%, #274b8e 35%, #d8c8d4 60%, #5a5060 100%); }
  .curtain-photo {
    position: absolute; left: 468px; top: 805px; width: 270px; height: 203px;
    background: linear-gradient(90deg, #ffffff 0%, #f1ece6 35%, #e6e2d8 65%, #8a8a3e 88%, #6c6d2a 100%);
  }
  .contact { position: absolute; font-size: 14px; line-height: 23px; }
  .contact .row { display: flex; align-items: flex-start; gap: 4px; }
  .contact svg { width: 12px; height: 12px; margin-top: 5px; flex: none; }
  .contact .indent { padding-left: 16px; }
  .contact.phone { left: 28px; top: 880px; }
  .contact.address { left: 28px; top: 948px; }
  .contact.online { left: 232px; top: 910px; }
  .footer-band { position: absolute; left: 0; bottom: 0; width: 100%; height: 27px; background: var(--ink); }
</style>
</head>
<body>
<main class="flyer">
  <header class="brand">
    <span class="brand-dot"></span>
    <span class="brand-name">KORU FLINT</span>
  </header>

  <div class="hero-photo" role="img" aria-label="Front-loading washing machines with an open door in a self-service laundry"></div>

  <svg class="offer-panel" viewBox="0 0 738 378" aria-hidden="true">
    <defs>
      <linearGradient id="panelFill" x1="0" y1="0" x2="1" y2="1">
        <stop offset="0" stop-color="#1fa9e1"/>
        <stop offset="1" stop-color="#5cc6ee"/>
      </linearGradient>
    </defs>
    <polygon points="373,0 738,0 738,378 448,378 458,358" fill="url(#panelFill)"/>
  </svg>

  <div class="offer-text">
    <div class="headline">CURTAIN</div>
    <div class="sub">LAUNDRY AT</div>
    <div class="price">$10/KG</div>
  </div>

  <ul class="services">
    <li class="service">
      <svg viewBox="0 0 30 30"><circle cx="15" cy="15" r="14" fill="var(--sky)" stroke="#0d6f99" stroke-width="1.5"/><rect x="7" y="11" width="10" height="7" fill="#fff"/><path d="M17 13h4l3 3v2h-7z" fill="#fff"/><circle cx="10" cy="19.5" r="1.8" fill="#0d6f99"/><circle cx="20" cy="19.5" r="1.8" fill="#0d6f99"/></svg>
      Include Pickup
    </li>
    <li class="service">
      <svg viewBox="0 0 30 30"><circle cx="15" cy="15" r="14" fill="var(--sky)" stroke="#0d6f99" stroke-width="1.5"/><circle cx="15" cy="15" r="6" fill="none" stroke="#fff" stroke-width="3"/><circle cx="15" cy="15" r="2" fill="#fff"/></svg>
      Installation
    </li>
    <li class="service">
      <svg viewBox="0 0 30 30"><circle cx="15" cy="15" r="14" fill="var(--sky)" stroke="#0d6f99" stroke-width="1.5"/><rect x="8" y="8" width="11" height="5" rx="1" fill="#fff" transform="rotate(-30 13 10)"/><rect x="13" y="12" width="3" height="11" fill="#fff" transform="rotate(-30 14 17)"/></svg>
      Dismantle
    </li>
    <li class="service">
      <svg viewBox="0 0 30 30"><circle cx="15" cy="15" r="14" fill="var(--sky)" stroke="#0d6f99" stroke-width="1.5"/><rect x="6" y="10" width="11" height="8" fill="#fff"/><path d="M17 12h4l3 3v3h-7z" fill="#fff"/><circle cx="10" cy="19.5" r="2" fill="#0d6f99"/><circle cx="20" cy="19.5" r="2" fill="#0d6f99"/></svg>
      Delivery
    </li>
  </ul>

  <div class="guarantee">
    <div class="line1">NO HIDDEN</div>
    <div class="line2">COST</div>
  </div>

  <div class="call-band">
    <div class="cta"><span>Call</span> 8362 4915</div>
  </div>

  <div class="shop-photo interior" role="img" aria-label="Inside the self-service laundry with rows of washers"></div>
  <div class="shop-photo storefront" role="img" aria-label="Laundry shop front at night"></div>

  <div class="curtain-photo" role="img" aria-label="Person opening clean curtains at a bright window"></div>

  <div class="contact phone">
    <div class="row"><svg viewBox="0 0 12 12"><rect x="2" y="0" width="8" height="12" rx="1.5" fill="var(--sky)"/><rect x="3.5" y="1.5" width="5" height="7" fill="#fff"/></svg>+65 8362 4915</div>
    <div class="indent">Reg No.71846302K</div>
  </div>

  <div class="contact address">
    <div class="row"><svg viewBox="0 0 12 12"><path d="M6 0L0 6h2v6h3V8h2v4h3V6h2z" fill="var(--sky)"/></svg>47 Merrowby Lane</div>
    <div class="indent">Singapore 071934</div>
  </div>

  <div class="contact online">
    <div class="row"><svg viewBox="0 0 12 12"><circle cx="6" cy="6" r="5.5" fill="var(--sky)"/><path d="M0.5 6h11M6 0.5c-3 3-3 8 0 11M6 0.5c3 3 3 8 0 11" stroke="#fff" stroke-width=".8" fill="none"/></svg>www.glintora.com.sg</div>
    <div class="row"><svg viewBox="0 0 12 12"><circle cx="6" cy="6" r="5.5" fill="var(--sky)"/><path d="M3 4.5h6v4H3zM3 4.5l3 2 3-2" stroke="#fff" stroke-width=".8" fill="none"/></svg>enquiries@glintora.com.sg</div>
  </div>

  <div class="footer-band"></div>
</main>
</body>
</html>
```